Business school needs a web design

Who We are:
KTRV is a small business school that offers programs in Project Management. The school is based in West Africa and welcomes students from the whole area. Our aim is to become one of the reference business schools in Africa.

Project Brief:
The site will include all informations relevant for different types of visitors that we have: actual and future students, companies, mass media, future employees, ect. It will present information about subscription, list of programs, presentation of the school and its team,etc.

What We want:
This competition is for Design only no coding! We need design for two pages.
We did some wireframing for the home page and the list of programs page. We made them just to show how we imagine the website would look like. But we encourage creative designs, so you don't have to stick to the wireframe models.

Sites We like:
http://www.larchmontgate.example/
http://www.pelvarin.example/fr/etudes.html
http://www.qwd.example/mba/Pages/default.aspx

Color schemes
The logo of the school is red and black. So the color scheme of the website should match that. For the rest, it is opened to your imagination.
Updates

The payment for the project is now garanteed. Good luck to you all !

Target Market(s)

The target market is diversified because we have students of different ages, also company representatives or employees that might visit the website for recruitment purposes. But the majority of our audience should be aged between 20 - 30 years.

Industry/Entity Type

Small Business

Requirements
Must have
• The design must include two pages: a home page and another interior page : might be the list of programs or any other page relevant to the domain. The Home page must include a slide show at the beginning.
The background page must be white.
Nice to have
• The use of flat design for this project is preferred.
The use of Chirp bootstrap as a base for the design is an asset.

```html
<!DOCTYPE html>
<html lang="fr">
<head>
<meta charset="utf-8">
<title>KTRV - Business school</title>
<link href="https://fonts.googleapis.com/css2?family=Open+Sans:wght@400;600;700&display=swap" rel="stylesheet">
<style>
:root{
  --red:#c4161c;
  --red-dark:#a50f14;
  --ink:#222;
  --muted:#777;
  --link:#1f4fa0;
  --line:#e3e3e3;
  --panel:#f2f2f2;
  --footer:#0b0b0b;
  --footer-bottom:#1c1c1c;
}
*{box-sizing:border-box;margin:0;padding:0}
html,body{width:771px;height:1200px;overflow:hidden;background:#fff}
body{font-family:'Open Sans',Arial,sans-serif;color:var(--ink);position:relative}
a{text-decoration:none;color:inherit}
.abs{position:absolute}

/* header */
.brand{left:64px;top:22px;display:flex;align-items:center;gap:6px}
.brand-dot{width:18px;height:18px;border-radius:50%;background:#111}
.brand-name{font-size:28px;font-weight:700;color:var(--red);letter-spacing:1px}
.utility{right:70px;top:15px;font-size:8.5px;color:#666;display:flex;gap:7px}
.utility span.sep{color:#bbb}
.search{left:589px;top:42px;width:118px;height:19px;border:1px solid #ccc;font-size:8px;color:#888;padding:4px 9px;display:flex;justify-content:space-between;align-items:center}
.mainnav{right:64px;top:73px;display:flex;gap:22px;font-size:11.5px;color:var(--red)}

/* hero */
.hero{left:0;top:106px;width:771px;height:276px;background:linear-gradient(180deg,#c9d3dc 0%,#8a9299 35%,#232a3b 70%,#1c2233 100%)}
.hero-caption{left:64px;top:226px;width:318px;height:114px;background:rgba(196,22,28,.88);border-right:3px solid #fff;padding:12px 18px;color:#fff}
.hero-caption .kicker{font-size:17px;line-height:20px}
.hero-caption .title{font-size:28px;line-height:32px}
.hero-caption p{font-size:8.5px;line-height:13px;margin-top:4px}
.dots{left:367px;top:366px;display:flex;gap:3px}
.dots i{width:8px;height:8px;border-radius:50%;background:#fff}

/* left column */
.box{border:1px solid #ddd;background:var(--panel)}
.box-head{background:#fff;height:28px;padding:7px 10px;font-size:11.5px;color:var(--red);border-bottom:1px solid #ddd}
.audience{left:64px;top:401px;width:153px}
.audience li{list-style:none;height:23.5px;line-height:23.5px;padding-left:10px;font-size:8.8px;border-bottom:1px solid #fff}
.tv{left:64px;top:609px;width:153px;height:121px}
.tv-media{height:93px;background:linear-gradient(135deg,#8d8a86,#4a4a4f 60%,#2d2e33);position:relative}
.more{font-size:8.8px;color:var(--link)}

/* main column */
.intro-title{left:233px;top:405px;font-size:14.5px;color:var(--red)}
.intro-text{left:233px;top:427px;width:305px;font-size:8.8px;line-height:14.5px;color:var(--muted)}
.rule{height:1px;background:var(--line);width:307px;left:233px}
.section-title{font-size:14px;color:var(--red)}
.post{width:95px}
.post-img{height:59px}
.post h3{font-size:9px;font-weight:400;margin-top:12px}
.post p{font-size:7.4px;line-height:10.8px;color:var(--muted);margin-top:3px}
.post .author{font-size:7.4px;color:var(--link);margin-top:4px}
.post .readmore{font-size:7.4px;color:var(--link);text-decoration:underline;margin-top:2px}
.event{left:233px;width:305px;display:flex;gap:8px}
.date{width:41px;height:42px;background:#6e6e6e;color:#fff;text-align:center;flex:none}
.date .m{font-size:8px;padding-top:6px}
.date .d{font-size:16px;font-weight:600;line-height:16px}
.event h4{font-size:9px;font-weight:400}
.event p{font-size:7.4px;line-height:10.2px;color:var(--muted);margin-top:3px}

/* news */
.news{left:554px;top:401px;width:153px;height:484px}
.news-item{display:flex;gap:7px;padding:8px 0 8px 8px;margin:0 3px;height:60.5px;border-bottom:1px solid #ddd}
.news-thumb{width:44px;height:40px;flex:none;border:2px solid #fff}
.news-item h4{font-size:8.6px;font-weight:400}
.news-item p{font-size:7.3px;line-height:10.3px;color:var(--muted);margin-top:2px}

/* share tab */
.share{left:738px;top:494px;width:33px;height:126px;background:var(--red);display:flex;flex-direction:column;align-items:center;justify-content:space-around;padding:6px 0;color:#fff;font-size:8px;font-weight:700}

/* partners */
.partners{left:0;top:906px;width:771px;height:66px;background:#ececec;display:flex;align-items:center;justify-content:center;gap:34px}
.partners span{font-size:15px;font-weight:700;color:var(--red)}

/* footer */
.footer{left:0;top:972px;width:771px;height:178px;background:var(--footer);color:#ddd}
.fcol{top:30px}
.fcol h5{font-size:12.5px;font-weight:400;color:#fff;margin-bottom:8px}
.fcol li{list-style:none;font-size:8.2px;line-height:16px}
.fcol p{font-size:8px;line-height:12.5px;color:#aaa}
.socials{display:flex;gap:8px;font-size:9px;font-weight:700;color:#fff;margin-top:14px}
.phone{display:flex;align-items:center;gap:4px;font-size:9.5px;margin-top:4px}
.email{width:132px;height:20px;border:1px solid #555;border-radius:2px;font-size:8px;color:#aaa;padding:4px 8px;margin-top:9px}
.signup{margin:7px 0 0 82px;width:50px;height:18px;background:var(--red);color:#fff;font-size:8px;text-align:center;line-height:18px;border-radius:2px}
.bottom{left:0;top:1150px;width:771px;height:50px;background:var(--footer-bottom);font-size:8px;color:#999;padding:18px 66px}
</style>
</head>
<body>

<header>
  <a class="brand abs" href="#"><span class="brand-dot"></span><span class="brand-name">KTRV</span></a>
  <nav class="utility abs">
    <a href="#">REPERTOIRE DU PERSONEL</a><span class="sep">/</span>
    <a href="#">BLOGUE</a><span class="sep">/</span>
    <a href="#">SALLE DE PRESSE</a><span class="sep">/</span>
    <a href="#">NOUS JOINDRE</a><span class="sep">/</span>
    <a href="#">FRANCAIS</a>
  </nav>
  <div class="search abs">Search
    <svg width="10" height="10" viewBox="0 0 10 10"><circle cx="4" cy="4" r="3" fill="none" stroke="#333" stroke-width="1.6"/><line x1="6" y1="6" x2="9.3" y2="9.3" stroke="#333" stroke-width="2"/></svg>
  </div>
  <nav class="mainnav abs">
    <a href="#">A Propos de l'KTRV</a>
    <a href="#">Programmes et Formations</a>
    <a href="#">Etudiants</a>
    <a href="#">Nouvelles et Everments</a>
    <a href="#">Enterprises</a>
  </nav>
</header>

<section class="hero abs" role="img" aria-label="Photo de groupe de diplômés en toge et toque devant un paysage urbain"></section>
<div class="hero-caption abs">
  <div class="kicker">Business school that offers</div>
  <div class="title">Project Management</div>
  <p>Class aptent taciti sociosqu ad litora torquent per conubia nostra, per inceptos hymenaeos Proin nulla arcu</p>
</div>
<div class="dots abs"><i></i><i></i><i></i></div>

<aside class="audience box abs">
  <div class="box-head">VOUS ETES</div>
  <ul>
    <li>Futur etudiant</li><li>Etudiant actuel</li><li>Enterprise</li><li>Employeur</li><li>Postulant</li><li>Medias</li><li style="border:0">Partenaires</li>
  </ul>
</aside>
<aside class="tv box abs">
  <div class="box-head">KTRV.TV</div>
  <div class="tv-media" role="img" aria-label="Vidéo : poignée de main entre hommes d'affaires">
    <svg class="abs" style="left:58px;top:28px" width="36" height="36" viewBox="0 0 36 36"><circle cx="18" cy="18" r="16" fill="none" stroke="#fff" stroke-width="2.5"/><path d="M14 11 L26 18 L14 25 Z" fill="#fff"/></svg>
  </div>
</aside>
<a class="more abs" style="left:65px;top:734px" href="#">+ de videos</a>

<main>
  <h1 class="intro-title abs" style="font-weight:400">KTRV : devenez les gestionnaires de demain</h1>
  <p class="intro-text abs">Nam rhoncus purus at neque fringilla, non eleifend nulla egestas. Nunc elementum aliquet eleifend. Donec rutrum nunc vitae lacus pellentesque facilisis. Phasellus condimentum eros vel felis sagittis tincidunt. Vivamus pellentesque dictum odio, et suscipit nulla posuere sit amet.</p>
  <div class="rule abs" style="top:500px"></div>

  <h2 class="section-title abs" style="left:233px;top:510px;font-weight:400">Blogue</h2>
  <article class="post abs" style="left:233px;top:541px">
    <div class="post-img" role="img" aria-label="Réunion d'équipe autour d'une table" style="background:linear-gradient(135deg,#e8e4df,#a89a8d)"></div>
    <h3>Morbi nisl sapien</h3>
    <p>Nunc euismod mi purus, id tincidunt sem porttitor sit amet. Sed in egestas odio. Suspendisse turpis mi, vehicula sed.</p>
    <div class="author">Paul Serin</div><div class="readmore">Line la suite</div>
  </article>
  <article class="post abs" style="left:338px;top:541px">
    <div class="post-img" role="img" aria-label="Mains travaillant sur des documents financiers" style="background:linear-gradient(135deg,#dfe4ec,#7c8798)"></div>
    <h3>Morbi nisl sapien</h3>
    <p>Nunc euismod mi purus, id tincidunt sem porttitor sit amet. Sed in egestas odio. Suspendisse turpis mi, vehicula sed.</p>
    <div class="author">Paul Serin</div><div class="readmore">Line la suite</div>
  </article>
  <article class="post abs" style="left:444px;top:541px">
    <div class="post-img" role="img" aria-label="Cadenas numérique sur fond bleu" style="background:linear-gradient(135deg,#0c3a78,#1f84d1 55%,#0a2850)"></div>
    <h3>Morbi nisl sapien</h3>
    <p>Nunc euismod mi purus, id tincidunt sem porttitor sit amet. Sed in egestas odio. Suspendisse turpis mi, vehicula sed.</p>
    <div class="author">Paul Serin</div><div class="readmore">Line la suite</div>
  </article>
  <div class="rule abs" style="top:722px"></div>

  <h2 class="section-title abs" style="left:233px;top:731px;font-weight:400">Evenements</h2>
  <div class="event abs" style="top:760px">
    <div class="date"><div class="m">Jan</div><div class="d">7</div></div>
    <div><h4>Pellentesque habitant</h4><p>Morbi interdum egestas felis, a vestibulum turpis accumsan a. Aliquam sed molestie risus. Mauris dapibus dolor at dui condimentum, in tempus nisi aliquam</p></div>
  </div>
  <div class="event abs" style="top:820px">
    <div class="date"><div class="m">Jan</div><div class="d">7</div></div>
    <div><h4>Pellentesque habitant</h4><p>Morbi interdum egestas felis, a vestibulum turpis accumsan a. Aliquam sed molestie risus. Mauris dapibus dolor at dui condimentum, in tempus nisi aliquam</p></div>
  </div>
  <a class="more abs" style="left:233px;top:877px" href="#">Tous les evenements</a>
</main>

<aside class="news box abs">
  <div class="box-head">NOUVELLES</div>
  <div class="news-item"><div class="news-thumb" role="img" aria-label="Tableau avec des mots-clés" style="background:linear-gradient(135deg,#d6dde3,#7d8d9b)"></div><div><h4>Quisque ligula ligula</h4><p>Donec est enim, luctus sed metus quis</p></div></div>
  <div class="news-item"><div class="news-thumb" role="img" aria-label="Hommes d'affaires se serrant la main" style="background:linear-gradient(135deg,#f1f1f1,#3a3d45)"></div><div><h4>Quisque ligula ligula</h4><p>Donec est enim, luctus sed metus quis</p></div></div>
  <div class="news-item"><div class="news-thumb" role="img" aria-label="Balle anti-stress bleue" style="background:linear-gradient(135deg,#e23a2a,#2f5fd1)"></div><div><h4>Quisque ligula ligula</h4><p>Donec est enim, luctus sed metus quis</p></div></div>
  <div class="news-item"><div class="news-thumb" role="img" aria-label="Personne au bureau avec ordinateur" style="background:linear-gradient(135deg,#eef2e6,#9aa58c)"></div><div><h4>Quisque ligula ligula</h4><p>Donec est enim, luctus sed metus quis</p></div></div>
  <div class="news-item"><div class="news-thumb" role="img" aria-label="Femme d'affaires souriante" style="background:linear-gradient(135deg,#f4f4f4,#6b5548)"></div><div><h4>Quisque ligula ligula</h4><p>Donec est enim, luctus sed metus quis</p></div></div>
  <div class="news-item"><div class="news-thumb" role="img" aria-label="Équipe professionnelle en réunion" style="background:linear-gradient(135deg,#e9e9e9,#444a55)"></div><div><h4>Quisque ligula ligula</h4><p>Donec est enim, luctus sed metus quis</p></div></div>
  <div class="news-item"><div class="news-thumb" role="img" aria-label="Collègues debout au bureau" style="background:linear-gradient(135deg,#ececec,#4f545c)"></div><div><h4>Quisque ligula ligula</h4><p>Donec est enim, luctus sed metus quis</p></div></div>
  <a class="more" style="display:block;padding:9px 9px" href="#">+ de nouvelles</a>
</aside>

<div class="share abs">
  <span>Nv</span><span>Lk</span><span>Ch</span>
  <svg width="16" height="14" viewBox="0 0 16 14"><rect x="4" y="0" width="8" height="4" fill="#fff"/><rect x="0" y="4" width="16" height="6" rx="1" fill="#fff"/><rect x="4" y="8" width="8" height="6" fill="#fff" stroke="#c4161c"/></svg>
  <svg width="16" height="14" viewBox="0 0 16 14"><rect x="0" y="0" width="16" height="10" rx="4" fill="#fff"/><path d="M3 9 L3 14 L8 9 Z" fill="#fff"/></svg>
</div>

<section class="partners abs">
  <span>Tallyleaf</span><span>Brightmark</span><span>Northvale</span><span>Quillset</span><span>Orbane</span><span>Harlowe</span>
</section>

<footer class="footer abs">
  <div class="fcol abs" style="left:63px">
    <h5>Get In Touch</h5>
    <div class="socials"><span>Nova</span><span>Linka</span><span>Chirp</span><span>Vidz</span></div>
  </div>
  <div class="fcol abs" style="left:187px">
    <h5>A propos</h5>
    <ul><li>A propos de KTRV</li><li>Admissions</li><li>Calender de ecole</li><li>Offres d' emplai</li><li>Pepertoire du personnel</li></ul>
  </div>
  <div class="fcol abs" style="left:314px">
    <h5>A propos</h5>
    <ul><li>A propos de KTRV</li><li>Admissions</li><li>Calender de ecole</li><li>Offres d' emplai</li><li>Pepertoire du personnel</li></ul>
  </div>
  <div class="fcol abs" style="left:433px;width:125px">
    <h5>KTRV</h5>
    <p style="color:#ddd">12, RUE DES ACACIAS Ancienne route, pres du marche des Artisans</p>
    <div class="phone" style="margin-top:6px"><svg width="10" height="10" viewBox="0 0 10 10"><path d="M2 0 L4 2.5 L3 4 Q4.5 6 6 7 L7.5 6 L10 8 L8.5 10 Q3 9 0 1.5 Z" fill="#ddd"/></svg>(221) 30 412 77 18</div>
    <div class="phone"><svg width="10" height="10" viewBox="0 0 10 10"><path d="M2 0 L4 2.5 L3 4 Q4.5 6 6 7 L7.5 6 L10 8 L8.5 10 Q3 9 0 1.5 Z" fill="#ddd"/></svg>(221) 70 245 93 06</div>
  </div>
  <div class="fcol abs" style="left:574px;width:140px">
    <h5>Newseletters Sign Up</h5>
    <p>Class aptent taciti sociosqu ad litora torquent per conubia nostra, per inceptos hymenaeos Proin nulla</p>
    <div class="email">email address</div>
    <div class="signup">SIGN UP</div>
  </div>
</footer>
<div class="bottom abs">© 2014 Company Name.&nbsp; All right reserved.&nbsp; Term of Use</div>

</body>
</html>
```